Surface Protection company needs cards

We are a New Zealand company that will apply nanotechnology coatings on surfaces to prevent growth and spread of bacteria, viruses, mold etc with a sprayer. We deal with large corporates, airlines, hospitals and schools so we are after a new modern, simple and clean look that will have great visual impact.
We a company that is focused on prevention and protection.

Company name, Vela Shield

Subtext, Antimicrobial Surface Protection

Logo, VS

Target Market(s)

Hospitals, Transport agencies, Airlines, Corporate entities

Contact Information for Business Card

Company name, VelaShield
Logo, VS

Gareth Tolley
velashieldnz@postbox.example
+64219305562
www.velashield.example.nz

Requirements
Must have
• Simple clean look.
Nice to have
• We apply nano coatings so try and incorporate this into a theme somehow

```html
<!DOCTYPE html>
<html lang="en">
<head>
<meta charset="utf-8">
<title>Vela Shield — Business Cards</title>
<link rel="stylesheet" href="https://fonts.googleapis.com/css2?family=Montserrat:wght@400;500;700;800&family=Lato:wght@400&display=swap">
<style>
  :root {
    --page-bg: #181818;
    --card-top: #2e2e2e;
    --card-bottom: #222222;
    --brand-green: #7dc53a;
    --brand-blue: #1a73d9;
    --text-light: #f2f2f2;
    --text-muted: #d8d8d8;
  }
  * { box-sizing: border-box; margin: 0; padding: 0; }
  html, body {
    width: 1200px; height: 900px; overflow: hidden;
    background: var(--page-bg);
  }
  .sheet {
    width: 1200px; height: 900px;
    display: flex; flex-direction: column;
    align-items: center; justify-content: center; gap: 34px;
  }
  .card {
    position: relative;
    width: 700px; height: 400px;
    background: linear-gradient(160deg, var(--card-top), var(--card-bottom));
    border-bottom: 6px solid var(--brand-green);
    box-shadow: 0 12px 30px rgba(0,0,0,.55);
  }
  .brand { display: flex; flex-direction: column; align-items: center; }
  .brand__row { display: flex; align-items: center; gap: 14px; }
  .brand__dot {
    width: 22px; height: 22px; border-radius: 50%;
    background: var(--brand-blue);
  }
  .brand__name {
    font-family: "Montserrat", sans-serif; font-weight: 800;
    color: var(--brand-green); letter-spacing: .5px; line-height: 1;
  }
  .brand__tagline {
    font-family: "Lato", sans-serif; font-weight: 400;
    color: var(--text-light); text-transform: uppercase;
    margin-top: 10px; letter-spacing: .4px;
  }

  /* Front */
  .card--front { display: flex; align-items: center; justify-content: center; }
  .card--front .brand__name { font-size: 66px; }
  .card--front .brand__tagline { font-size: 17px; }

  /* Back */
  .card--back { display: flex; align-items: center; padding: 0 40px 0 46px; }
  .card--back .brand { width: 330px; }
  .card--back .brand__name { font-size: 46px; }
  .card--back .brand__tagline { font-size: 12.5px; }
  .divider {
    width: 2px; height: 150px; background: var(--brand-green);
    margin: 0 34px 0 24px;
  }
  .contact { font-family: "Montserrat", sans-serif; color: var(--text-light); }
  .contact__name {
    font-weight: 700; font-size: 25px; color: var(--brand-blue);
  }
  .contact__role { font-size: 17px; color: var(--text-muted); margin: 2px 0 22px; }
  .contact__list { list-style: none; display: flex; flex-direction: column; gap: 8px; }
  .contact__item { display: flex; align-items: center; gap: 12px; font-size: 15.5px; }
  .contact__icon { width: 15px; height: 15px; flex: none; }
  .contact__accent { color: var(--brand-green); }
</style>
</head>
<body>
<main class="sheet">
  <section class="card card--front" aria-label="Card front">
    <div class="brand">
      <div class="brand__row">
        <span class="brand__dot"></span>
        <h1 class="brand__name">Vela Shield</h1>
      </div>
      <p class="brand__tagline">Antimicrobial Surface Protection</p>
    </div>
  </section>

  <section class="card card--back" aria-label="Card back">
    <div class="brand">
      <div class="brand__row">
        <span class="brand__dot"></span>
        <h2 class="brand__name">Vela Shield</h2>
      </div>
      <p class="brand__tagline">Antimicrobial Surface Protection</p>
    </div>
    <div class="divider"></div>
    <div class="contact">
      <p class="contact__name">Gareth Tolley</p>
      <p class="contact__role">Director</p>
      <ul class="contact__list">
        <li class="contact__item">
          <svg class="contact__icon" viewBox="0 0 16 16" aria-hidden="true"><path d="M4 1.5l2.2 3-1.4 1.6c.8 1.9 2.3 3.4 4.2 4.3l1.6-1.4 3 2.2-1.2 2.6C7 13.6 2.4 9 1.4 2.7z" fill="none" stroke="#1a73d9" stroke-width="1.4" stroke-linejoin="round"/></svg>
          <span>+64219305562</span>
        </li>
        <li class="contact__item">
          <svg class="contact__icon" viewBox="0 0 16 16" aria-hidden="true"><rect x="1.5" y="3.5" width="13" height="9" fill="none" stroke="#1a73d9" stroke-width="1.4"/><path d="M1.5 3.5L8 9l6.5-5.5" fill="none" stroke="#1a73d9" stroke-width="1.4"/></svg>
          <span>velashieldnz@postbox.example</span>
        </li>
        <li class="contact__item">
          <svg class="contact__icon" viewBox="0 0 16 16" aria-hidden="true"><g fill="none" stroke="#1a73d9" stroke-width="1.3"><circle cx="8" cy="8" r="6.5"/><ellipse cx="8" cy="8" rx="3" ry="6.5"/><path d="M1.5 8h13M2.5 4.7h11M2.5 11.3h11"/></g></svg>
          <span>www.<span class="contact__accent">velashield</span>.example.nz</span>
        </li>
      </ul>
    </div>
  </section>
</main>
</body>
</html>
```